Walking Food Tour Business In Melbourne.

We need a two sided A4 page flyer
(1) Front Side - Detailing all the 'foodie' venue stops and other spots of interest. We have one already which is attached. What we are looking for is a better design - rather than just words running down the page. Perhaps something in clouds or boxes/circles relatable to food? However important to note, the venues need to change and therefore the 'user' needs to be able to update the page.
(2) Back Side - The back page, we are looking for a CBD map of Melbourne. I have attached one, but open to a more user friendly one if better suited.
Thank you

```html
<!DOCTYPE html>
<html lang="en">
<head>
<meta charset="utf-8">
<title>Laneway Walks – Foodies Bucket List Tour Flyer</title>
<link href="https://fonts.googleapis.com/css2?family=Montserrat:wght@400;500;600&family=Roboto:wght@400;500;700&display=swap" rel="stylesheet">
<style>
  :root {
    --backdrop: #3f4144;
    --paper: #ffffff;
    --ink: #2b2b2b;
    --ink-soft: #555555;
    --navy: #1d3a5c;
    --panel-grey: #7a7a7a;
    --swoosh-grey: #b4b4b4;
    --footer-black: #1d1d1d;
    --pill-navy: #16304d;
    --panel-text: #f2f2f2;
  }
  * { box-sizing: border-box; margin: 0; padding: 0; }
  html, body { width: 1200px; height: 1200px; overflow: hidden; }
  body {
    background: var(--backdrop);
    font-family: "Montserrat", sans-serif;
    color: var(--ink);
    position: relative;
  }
  .page {
    position: absolute;
    top: 218px;
    width: 540px;
    height: 764px;
    background: var(--paper);
    overflow: hidden;
    box-shadow: 0 6px 18px rgba(0,0,0,.35);
  }
  .page--front { left: 45px; }
  .page--back { left: 615px; }

  /* ---------- Front ---------- */
  .hero-photo {
    position: absolute; left: 0; top: 0; width: 540px; height: 420px;
    background: linear-gradient(180deg, #2f7fd6 0%, #8fc2ee 32%, #c9c3b4 52%, #6f7d86 66%, #4b5966 100%);
  }
  .page-shapes { position: absolute; left: 0; top: 0; }
  .food-photo {
    position: absolute; border-radius: 50%;
    border: 5px solid #b9b9b9;
  }
  .food-photo--large {
    left: 26px; top: 250px; width: 146px; height: 146px;
    background: radial-gradient(circle at 50% 50%, #f1d27a 0%, #6e9b3f 45%, #24381c 100%);
  }
  .food-photo--small {
    left: 158px; top: 272px; width: 112px; height: 112px;
    background: radial-gradient(circle at 50% 55%, #b5502f 0%, #d9cbb9 45%, #8c7a6a 100%);
  }
  .brand-mark--hero {
    position: absolute; right: 40px; top: 334px;
    font-family: "Montserrat", sans-serif; font-weight: 600;
    font-size: 20px; color: #ffffff;
  }

  .stops-list {
    position: absolute; left: 24px; top: 416px; width: 238px;
  }
  .stops-list__title {
    font-family: "Roboto", sans-serif; font-weight: 500;
    font-size: 16.5px; color: var(--ink); margin-bottom: 14px;
  }
  .stop { margin-bottom: 14px; }
  .stop__head {
    display: flex; justify-content: space-between;
    font-size: 7.6px; font-weight: 500; color: var(--navy);
    letter-spacing: .3px; margin-bottom: 5px;
  }
  .stop__name { text-transform: uppercase; }
  .stop__desc { font-size: 7px; line-height: 1.35; color: var(--ink-soft); }

  .spots-panel {
    position: absolute; left: 282px; top: 410px; width: 240px;
    color: var(--panel-text);
  }
  .spots-panel__title {
    font-family: "Roboto", sans-serif; font-weight: 500;
    font-size: 12.5px; margin-bottom: 10px; color: #ffffff;
  }
  .spot { margin-bottom: 8px; }
  .spot__name { font-size: 7.2px; font-weight: 600; margin-bottom: 3px; }
  .spot__desc { font-size: 6.8px; line-height: 1.38; }
  .spot-pair { display: flex; gap: 26px; }

  .contact-bar {
    position: absolute; left: 0; bottom: 0; width: 540px; height: 30px;
    background: var(--footer-black); color: #ffffff;
    display: flex; align-items: center; justify-content: center; gap: 26px;
    font-size: 10.5px;
  }
  .contact-bar__item { display: flex; align-items: center; gap: 7px; }
  .icon { width: 10px; height: 10px; flex: none; }

  /* ---------- Back ---------- */
  .laneway-photo {
    position: absolute; left: 0; top: 340px; width: 540px; height: 394px;
    background: linear-gradient(180deg, #ffffff 0%, #f0f0f0 35%, #d6d6d6 75%, #c9c9c9 100%);
  }
  .city-map {
    position: absolute; left: 24px; top: 36px; width: 504px; height: 314px;
    border-radius: 6px; border: 1px solid #d8d8d8;
    background: linear-gradient(135deg, #e4e4e4 0%, #cfcfcf 45%, #c6d98e 72%, #7fb3e0 100%);
  }
  .brand-mark--back {
    position: absolute; left: 0; top: 440px; width: 540px; text-align: center;
    font-family: "Montserrat", sans-serif; font-weight: 600;
    font-size: 30px; color: var(--ink);
  }
  .contact-block {
    position: absolute; left: 0; top: 540px; width: 540px;
    display: flex; flex-direction: column; align-items: center;
    color: var(--ink);
  }
  .contact-block__pill {
    background: var(--pill-navy); color: #ffffff;
    font-size: 11.5px; font-weight: 500; letter-spacing: .3px;
    padding: 2px 12px; border-radius: 10px; margin-bottom: 10px;
  }
  .contact-block__icon {
    width: 14px; height: 14px; margin-bottom: 4px;
  }
  .contact-block__line { font-size: 13px; margin-bottom: 10px; }
  .contact-block__follow { font-size: 11.5px; font-weight: 500; margin-top: 4px; }

  .social-bar {
    position: absolute; left: 0; bottom: 0; width: 540px; height: 42px;
    background: var(--footer-black);
    display: flex; justify-content: center; gap: 18px; padding-top: 8px;
  }
  .social-bar__dot { width: 19px; height: 19px; border-radius: 50%; background: #ffffff; }
</style>
</head>
<body>

<section class="page page--front">
  <div class="hero-photo" role="img" aria-label="Photo of a city river with a footbridge, moored tour boat, autumn trees and towers under a blue sky"></div>

  <svg class="page-shapes" width="540" height="764" viewBox="0 0 540 764" aria-hidden="true">
    <path d="M0,398 Q140,368 272,360 L272,376 Q140,384 0,414 Z" fill="var(--swoosh-grey)"/>
    <path d="M0,412 Q140,382 272,374 L272,734 L0,734 Z" fill="var(--paper)"/>
    <path d="M272,360 Q420,368 540,420 L540,734 L272,734 Z" fill="var(--panel-grey)"/>
  </svg>

  <div class="food-photo food-photo--large" role="img" aria-label="Photo of a salad bowl with halved boiled eggs and greens"></div>
  <div class="food-photo food-photo--small" role="img" aria-label="Photo of a plated restaurant dish"></div>

  <div class="brand-mark brand-mark--hero">Laneway Walks</div>

  <div class="stops-list">
    <h1 class="stops-list__title">Foodies Bucket List Tour</h1>

    <div class="stop">
      <div class="stop__head"><span class="stop__name">Hartley's Chocolate</span><span>Gallery Arcade</span></div>
      <p class="stop__desc">Founded in 1923 by Alfred Hartley from the coast. Signature Frog</p>
    </div>
    <div class="stop">
      <div class="stop__head"><span class="stop__name">Sombra Original</span><span>Tanner Lane</span></div>
      <p class="stop__desc">Tapas Bar &amp; Restaurant with a graffiti art exterior. Signature Anchoa &amp; Croqueta</p>
    </div>
    <div class="stop">
      <div class="stop__head"><span class="stop__name">Lotus Lane</span><span>Ashby Lane</span></div>
      <p class="stop__desc">Pan Asian street food flavours. An intriguing Asian influences from Shanghai, Hongkong, Seoul &amp; Japan Soft Shell Crab or Eggplant Pancake Roll</p>
    </div>
    <div class="stop">
      <div class="stop__head"><span class="stop__name">Pachacama</span><span>Foundry Lane</span></div>
      <p class="stop__desc">Peruvian bar and grill Peruano 'Snapper' Ceviche, Pastel De Choclo &amp; Alpaca Croquette</p>
    </div>
    <div class="stop">
      <div class="stop__head"><span class="stop__name">Stratus Inc</span><span>Foundry Lane</span></div>
      <p class="stop__desc">Described as a 'local' eatinghouse and bar, rather than a restaurant – this favourite with large industrial New York style windows is located in an old rag trade building. Lemon-curd Madeleine &amp; coffee/tea</p>
    </div>
  </div>

  <div class="spots-panel">
    <h2 class="spots-panel__title">Some Of Our Favourite Spots On Tour...</h2>

    <div class="spot">
      <div class="spot__name">Riverside Station</div>
      <p class="spot__desc">Completed 1911 this station now enjoys 90,000 commuters and 1200 trains daily</p>
    </div>
    <div class="spot">
      <div class="spot__name">Delmont Street</div>
      <p class="spot__desc">Originally a 'service' lane, now a vibrant &amp; lively laneway</p>
    </div>
    <div class="spot">
      <div class="spot__name">Gallery Arcade</div>
      <p class="spot__desc">Opened in 1894, visit this Italian designed shopping arcade for the Kensington Tea Rooms, Spicehaus Herb &amp; Spice Merchants &amp; Hartley's Chocolates</p>
    </div>
    <div class="spot">
      <div class="spot__name">Regent Arcade</div>
      <p class="spot__desc">Opened in 1872, this spectacular Victorian Arcade is the oldest in the city.</p>
    </div>
    <div class="spot">
      <div class="spot__name">Penrose Place</div>
      <p class="spot__desc">With kitschy, framed artworks lining the brick walls, &amp; an old-school laneway vibe. Killer brew at 30ml coffee &amp; cocktails at Cortado Bar</p>
    </div>
    <div class="spot">
      <div class="spot__name">Tanner Lane</div>
      <p class="spot__desc">Blue stone laneway with some of our cities best street art embraced</p>
    </div>
    <div class="spot-pair">
      <div class="spot">
        <div class="spot__name">Boardwalk Place</div>
        <p class="spot__desc">Marlowe Bar</p>
      </div>
      <div class="spot">
        <div class="spot__name">Hopyard Lane</div>
        <p class="spot__desc">Eau Claire Bar - Cocktails</p>
      </div>
    </div>
  </div>

  <footer class="contact-bar">
    <span class="contact-bar__item">
      <svg class="icon" viewBox="0 0 24 24" aria-hidden="true"><path d="M6.6 10.8a15.2 15.2 0 0 0 6.6 6.6l2.2-2.2a1 1 0 0 1 1-.25 11.4 11.4 0 0 0 3.6.57 1 1 0 0 1 1 1V20a1 1 0 0 1-1 1A17 17 0 0 1 3 4a1 1 0 0 1 1-1h3.5a1 1 0 0 1 1 1c0 1.25.2 2.45.57 3.57a1 1 0 0 1-.25 1z" fill="#fff"/></svg>
      0400 123 456
    </span>
    <span class="contact-bar__item">
      <svg class="icon" viewBox="0 0 24 24" aria-hidden="true"><rect x="2" y="5" width="20" height="14" rx="1.5" fill="#fff"/><path d="M2.5 6l9.5 7 9.5-7" stroke="#1d1d1d" stroke-width="1.6" fill="none"/></svg>
      hello@lanewaywalks.com
    </span>
    <span class="contact-bar__item">
      <svg class="icon" viewBox="0 0 24 24" aria-hidden="true"><circle cx="12" cy="12" r="9.5" stroke="#fff" stroke-width="1.8" fill="none"/><ellipse cx="12" cy="12" rx="4" ry="9.5" stroke="#fff" stroke-width="1.6" fill="none"/><path d="M2.5 12h19" stroke="#fff" stroke-width="1.6"/></svg>
      www.lanewaywalks.com
    </span>
  </footer>
</section>

<section class="page page--back">
  <div class="laneway-photo" role="img" aria-label="Faded black and white photo of a busy city laneway with cafes"></div>
  <div class="city-map" role="img" aria-label="City centre street map with legend, parks, river and tram routes"></div>

  <div class="brand-mark brand-mark--back">Laneway Walks</div>

  <div class="contact-block">
    <span class="contact-block__pill">CONTACT US</span>
    <svg class="contact-block__icon" viewBox="0 0 24 24" aria-hidden="true"><circle cx="12" cy="12" r="11" fill="#8a8a8a"/><path d="M8.6 10.9a8.3 8.3 0 0 0 4.5 4.5l1.4-1.4a.6.6 0 0 1 .6-.15 6.7 6.7 0 0 0 2 .33.6.6 0 0 1 .6.6V17a.6.6 0 0 1-.6.6A10 10 0 0 1 6.4 7.2a.6.6 0 0 1 .6-.6h2.2a.6.6 0 0 1 .6.6c0 .7.1 1.4.33 2a.6.6 0 0 1-.15.6z" fill="#fff"/></svg>
    <span class="contact-block__line">0400 123 456</span>
    <svg class="contact-block__icon" viewBox="0 0 24 24" aria-hidden="true"><circle cx="12" cy="12" r="11" fill="#8a8a8a"/><rect x="6.5" y="8" width="11" height="8" rx="1" fill="#fff"/><path d="M7 8.6l5 3.8 5-3.8" stroke="#8a8a8a" stroke-width="1" fill="none"/></svg>
    <span class="contact-block__line">hello@lanewaywalks.com</span>
    <svg class="contact-block__icon" viewBox="0 0 24 24" aria-hidden="true"><circle cx="12" cy="12" r="11" fill="#8a8a8a"/><circle cx="12" cy="12" r="6" stroke="#fff" stroke-width="1.2" fill="none"/><ellipse cx="12" cy="12" rx="2.5" ry="6" stroke="#fff" stroke-width="1" fill="none"/><path d="M6 12h12" stroke="#fff" stroke-width="1"/></svg>
    <span class="contact-block__line">www.lanewaywalks.com</span>
    <span class="contact-block__follow">FOLLOW US</span>
  </div>

  <footer class="social-bar">
    <span class="social-bar__dot" aria-label="Social profile"></span>
    <span class="social-bar__dot" aria-label="Social profile"></span>
  </footer>
</section>

</body>
</html>
```